RB's Sports Bar Menu (Cape Cod Sports Bar)

We are a new england sports bar based on Cape Cod.

We are an old school type sports bar with pizza and wings type food.

We want to highlight our pizza as the main draw on our menu.

The style we are looking for is a placemat menu that looks casual and fun.

We want the following sections:
Starters:

Soups:

Salads:

Handhelds:

Plates:

Sides:

Desserts:

I can provide a draft of all the menu items upon request didn't want to overload this text box thank you!

• The menu must be LANDSCAPE design as it is going on a paper placemat. It also needs to all fit on ONE SIDE.

```html
<!DOCTYPE html>
<html lang="en">
<head>
<meta charset="utf-8">
<title>RB's Sports Bar – Placemat Menu</title>
<link rel="stylesheet" href="https://fonts.googleapis.com/css2?family=Almendra+SC&family=Montserrat:wght@400;700&display=swap">
<style>
  :root {
    --page-bg: #a9a9a9;
    --menu-red: #8b2a2e;
    --band-red: rgba(139, 42, 46, 0.88);
    --heading-yellow: #f6d518;
    --item-white: #ffffff;
    --photo-dark: #5a3a2a;
    --photo-mid: #8a5a3c;
    --photo-warm: #a8432f;
  }
  * { margin: 0; padding: 0; box-sizing: border-box; }
  html, body { width: 1200px; height: 1200px; overflow: hidden; }
  body { background: var(--page-bg); position: relative; font-family: "Montserrat", sans-serif; }

  .placemat {
    position: absolute; left: 60px; top: 219px;
    width: 1080px; height: 762px;
    background: var(--menu-red);
    overflow: hidden;
  }

  .hero-photo {
    position: absolute; left: 0; top: 0; width: 361px; height: 100%;
    background: linear-gradient(160deg, var(--photo-dark) 0%, var(--photo-mid) 50%, var(--photo-dark) 100%);
  }
  .brand-band {
    position: absolute; left: 0; top: 246px; width: 361px; height: 270px;
    background: var(--band-red);
    display: flex; align-items: center; justify-content: center;
  }
  .brand-name {
    color: var(--item-white); font-family: "Montserrat", sans-serif;
    font-weight: 700; font-size: 44px; line-height: 1.1; text-align: center;
  }

  .menu-section { position: absolute; width: 307px; }
  .menu-section h2 {
    font-family: "Almendra SC", serif; font-weight: 400;
    color: var(--heading-yellow); font-size: 20px; letter-spacing: 0.5px;
    line-height: 20px; margin-bottom: 31px;
  }
  .menu-items { list-style: none; }
  .menu-item {
    display: flex; align-items: baseline;
    color: var(--item-white); font-size: 15px; line-height: 18.5px;
  }
  .menu-item .leader { flex: 1; border-bottom: 1.5px dotted var(--item-white); margin: 0 2px; transform: translateY(-4px); }

  .col-left { left: 387px; }
  .col-right { left: 746px; }
  .starters { top: 33px; }
  .soups { top: 217px; }
  .salads { top: 402px; }
  .handhelds { top: 578px; }
  .plates { top: 33px; }
  .sides { top: 227px; }
  .desserts { top: 421px; }

  .pizza-photo {
    position: absolute; left: 721px; top: 581px; width: 359px; height: 181px;
    background: linear-gradient(180deg, rgba(168, 67, 47, 0) 0%, var(--photo-warm) 45%, var(--photo-dark) 100%);
  }
</style>
</head>
<body>
  <main class="placemat">
    <div class="hero-photo" role="img" aria-label="Photo of a pizza on a wooden table with basil, garlic, olive oil and a pizza cutter"></div>
    <div class="brand-band">
      <h1 class="brand-name">RB's<br>Sports Bar</h1>
    </div>

    <section class="menu-section col-left starters">
      <h2>Starters:</h2>
      <ul class="menu-items">
        <li class="menu-item"><span>StartersStartersStarter</span><span class="leader"></span><span>$60</span></li>
        <li class="menu-item"><span>StartersStartersStarter</span><span class="leader"></span><span>$60</span></li>
        <li class="menu-item"><span>StartersStartersStarter</span><span class="leader"></span><span>$60</span></li>
        <li class="menu-item"><span>StartersStartersStarter</span><span class="leader"></span><span>$60</span></li>
        <li class="menu-item"><span>StartersStartersStarter</span><span class="leader"></span><span>$60</span></li>
        <li class="menu-item"><span>StartersStartersStarter</span><span class="leader"></span><span>$60</span></li>
      </ul>
    </section>
    <section class="menu-section col-left soups">
      <h2>Soups:</h2>
      <ul class="menu-items">
        <li class="menu-item"><span>StartersStartersStarter</span><span class="leader"></span><span>$60</span></li>
        <li class="menu-item"><span>StartersStartersStarter</span><span class="leader"></span><span>$60</span></li>
        <li class="menu-item"><span>StartersStartersStarter</span><span class="leader"></span><span>$60</span></li>
        <li class="menu-item"><span>StartersStartersStarter</span><span class="leader"></span><span>$60</span></li>
        <li class="menu-item"><span>StartersStartersStarter</span><span class="leader"></span><span>$60</span></li>
        <li class="menu-item"><span>StartersStartersStarter</span><span class="leader"></span><span>$60</span></li>
      </ul>
    </section>
    <section class="menu-section col-left salads">
      <h2>Salads:</h2>
      <ul class="menu-items">
        <li class="menu-item"><span>StartersStartersStarter</span><span class="leader"></span><span>$60</span></li>
        <li class="menu-item"><span>StartersStartersStarter</span><span class="leader"></span><span>$60</span></li>
        <li class="menu-item"><span>StartersStartersStarter</span><span class="leader"></span><span>$60</span></li>
        <li class="menu-item"><span>StartersStartersStarter</span><span class="leader"></span><span>$60</span></li>
        <li class="menu-item"><span>StartersStartersStarter</span><span class="leader"></span><span>$60</span></li>
        <li class="menu-item"><span>StartersStartersStarter</span><span class="leader"></span><span>$60</span></li>
      </ul>
    </section>
    <section class="menu-section col-left handhelds">
      <h2>Handhelds:</h2>
      <ul class="menu-items">
        <li class="menu-item"><span>StartersStartersStarter</span><span class="leader"></span><span>$60</span></li>
        <li class="menu-item"><span>StartersStartersStarter</span><span class="leader"></span><span>$60</span></li>
        <li class="menu-item"><span>StartersStartersStarter</span><span class="leader"></span><span>$60</span></li>
        <li class="menu-item"><span>StartersStartersStarter</span><span class="leader"></span><span>$60</span></li>
        <li class="menu-item"><span>StartersStartersStarter</span><span class="leader"></span><span>$60</span></li>
        <li class="menu-item"><span>StartersStartersStarter</span><span class="leader"></span><span>$60</span></li>
      </ul>
    </section>

    <section class="menu-section col-right plates">
      <h2>Plates:</h2>
      <ul class="menu-items">
        <li class="menu-item"><span>StartersStartersStarter</span><span class="leader"></span><span>$60</span></li>
        <li class="menu-item"><span>StartersStartersStarter</span><span class="leader"></span><span>$60</span></li>
        <li class="menu-item"><span>StartersStartersStarter</span><span class="leader"></span><span>$60</span></li>
        <li class="menu-item"><span>StartersStartersStarter</span><span class="leader"></span><span>$60</span></li>
        <li class="menu-item"><span>StartersStartersStarter</span><span class="leader"></span><span>$60</span></li>
        <li class="menu-item"><span>StartersStartersStarter</span><span class="leader"></span><span>$60</span></li>
      </ul>
    </section>
    <section class="menu-section col-right sides">
      <h2>Sides:</h2>
      <ul class="menu-items">
        <li class="menu-item"><span>StartersStartersStarter</span><span class="leader"></span><span>$60</span></li>
        <li class="menu-item"><span>StartersStartersStarter</span><span class="leader"></span><span>$60</span></li>
        <li class="menu-item"><span>StartersStartersStarter</span><span class="leader"></span><span>$60</span></li>
        <li class="menu-item"><span>StartersStartersStarter</span><span class="leader"></span><span>$60</span></li>
        <li class="menu-item"><span>StartersStartersStarter</span><span class="leader"></span><span>$60</span></li>
        <li class="menu-item"><span>StartersStartersStarter</span><span class="leader"></span><span>$60</span></li>
      </ul>
    </section>
    <section class="menu-section col-right desserts">
      <h2>Desserts:</h2>
      <ul class="menu-items">
        <li class="menu-item"><span>StartersStartersStarter</span><span class="leader"></span><span>$60</span></li>
        <li class="menu-item"><span>StartersStartersStarter</span><span class="leader"></span><span>$60</span></li>
        <li class="menu-item"><span>StartersStartersStarter</span><span class="leader"></span><span>$60</span></li>
        <li class="menu-item"><span>StartersStartersStarter</span><span class="leader"></span><span>$60</span></li>
        <li class="menu-item"><span>StartersStartersStarter</span><span class="leader"></span><span>$60</span></li>
        <li class="menu-item"><span>StartersStartersStarter</span><span class="leader"></span><span>$60</span></li>
      </ul>
    </section>

    <div class="pizza-photo" role="img" aria-label="Photo of a sliced pizza with tomatoes and basil"></div>
  </main>
</body>
</html>
```